TR Stationery - Modern Contemporary

Develop modern template for Letterhead and Stationery (business card, letterhead, envelopes) using the TR Logo and Icon

Colors
0054AA
0677BA
7BADD7
CADEEF
E8F1F8
00AB8E
00BBA5
67D7C9
C6EFE9
E9F9F6
EE7325
F08F49
F5BC92
FAE3D3
FDF4ED
6B429C
8869AF
B7A5CE
E3DAEB
F3F0F8

```html
<!DOCTYPE html>
<html lang="en">
<head>
<meta charset="utf-8">
<title>TR Stationery – Letterhead Samples</title>
<link href="https://fonts.googleapis.com/css2?family=Figtree:ital,wght@0,400;0,500;0,600;0,700;1,400&display=swap" rel="stylesheet">
<style>
  :root{
    --board:#a8a8a8;
    --board-light:#b4b4b4;
    --paper:#ffffff;
    --ink:#1e2340;
    --text:#1b1b1b;
    --green:#1fae62;
    --orange:#ee7325;
    --rule-navy:#3b3f66;
    --pattern:#f1f1f1;
    --faint:#f2f2f2;
    --label:#ffffff;
  }
  *{margin:0;padding:0;box-sizing:border-box}
  html,body{width:1200px;height:768px;overflow:hidden}
  body{
    position:relative;
    background:radial-gradient(ellipse at 50% 45%,var(--board-light),var(--board) 75%);
    font-family:"Figtree",Arial,sans-serif;
    color:var(--text);
  }
  .sample-label{
    position:absolute;bottom:88px;
    transform-origin:left bottom;transform:rotate(-90deg);
    color:var(--label);font-size:22px;font-weight:400;letter-spacing:1px;
    white-space:nowrap;
  }
  .sample-label.one{left:80px}
  .sample-label.two{left:652px}

  .sheet{
    position:absolute;top:64px;width:440px;height:621px;
    background:var(--paper);overflow:hidden;
    box-shadow:-14px 18px 30px rgba(0,0,0,.28);
  }
  .sheet.one{left:106px}
  .sheet.two{left:676px}

  .pattern-fill{
    position:absolute;inset:0;
    background:linear-gradient(160deg,#f6f6f6,var(--pattern) 60%,#f4f4f4);
  }
  .big-initials{
    position:absolute;right:-6px;top:440px;
    font-size:150px;font-weight:700;line-height:1;letter-spacing:-4px;
    color:var(--faint);
  }
  .sheet.one .big-initials{color:#ebebeb}

  .wordmark{
    position:absolute;left:43px;
    font-weight:700;color:var(--ink);letter-spacing:-.5px;
    line-height:1;white-space:nowrap;
  }
  .sheet.one .wordmark{top:30px;font-size:44px}
  .sheet.two .wordmark{top:34px;font-size:37px}
  .header-rule{
    position:absolute;left:258px;top:62px;width:138px;height:1.5px;
    background:var(--orange);
  }

  .recipient{position:absolute;left:43px}
  .sheet.one .recipient{top:136px}
  .sheet.two .recipient{top:143px}
  .person-name{font-size:10.5px;font-weight:600;color:var(--text)}
  .person-role{font-size:7px;font-style:italic;margin-top:4px}

  .letter-body{
    position:absolute;left:42px;top:182px;width:354px;
    font-size:6.95px;line-height:8.9px;text-align:justify;color:var(--text);
  }
  .letter-body p+p{margin-top:8.9px}

  .signature{
    position:absolute;left:43px;top:428px;width:88px;height:44px;
    background:linear-gradient(120deg,rgba(30,35,64,.08),rgba(30,35,64,.03));
    border-radius:3px;
  }
  .signoff{position:absolute;left:43px;top:476px}

  .footer-rule{position:absolute;height:1px}
  .sheet.one .footer-rule{left:43px;top:576px;width:353px;background:var(--rule-navy)}
  .sheet.two .footer-rule{left:25px;top:576px;width:384px;background:var(--green)}

  .contact{
    position:absolute;display:flex;align-items:center;gap:6px;
    font-size:7px;line-height:9px;color:var(--text);
  }
  .contact svg{width:20px;height:20px;flex:none}
  .sheet.one .contact{top:588px}
  .sheet.two .contact{top:585px}
  .sheet.one .contact.address{left:41px}
  .sheet.one .contact.phone{left:184px}
  .sheet.one .contact.web{left:295px}
  .sheet.two .contact.address{left:42px}
  .sheet.two .contact.phone{left:185px}
  .sheet.two .contact.web{left:296px}
</style>
</head>
<body>

<span class="sample-label one">SAMPLE 1</span>
<span class="sample-label two">SAMPLE 2</span>

<!-- Letterhead variant one: patterned background -->
<section class="sheet one">
  <div class="pattern-fill" role="img" aria-label="Faint repeating brand-name pattern across the sheet"></div>
  <div class="big-initials">TR</div>
  <div class="wordmark">toren ridge</div>

  <div class="recipient">
    <div class="person-name">Name Goes Here</div>
    <div class="person-role">Designation here</div>
  </div>

  <div class="letter-body">
    <p>Lorem Ipsum is simply dummy text of the printing and typesetting industry. Lorem Ipsum has been the industry's standard dummy text ever since the 1500s, when an unknown printer took a galley of type and scrambled it to make a type specimen book. It has survived not only five centuries, but also the leap into electronic typesetting, remaining essentially unchanged. It was popularised in the 1960s with the release of Markwell sheets containing Lorem Ipsum passages, and more recently with desktop publishing software like Orvel PageForge including versions of Lorem Ipsum. Lorem Ipsum is simply dummy text of the printing and typesetting industry. Lorem Ipsum has been the industry's standard dummy text ever since the 1500s, when an unknown printer took a galley of type and scrambled it to make a type specimen book.</p>
    <p>Lorem Ipsum is simply dummy text of the printing and typesetting industry. Lorem Ipsum has been the industry's standard dummy text ever since the 1500s, when an unknown printer took a galley of type and scrambled it to make a type specimen book. It has survived not only five centuries, but also the leap into electronic typesetting, remaining essentially unchanged. It was popularised in the 1960s with the release of Markwell sheets containing Lorem Ipsum passages, and more recently with desktop publishing software like Orvel PageForge including versions of Lorem Ipsum. Lorem Ipsum is simply dummy text of the printing and typesetting industry. Lorem Ipsum has been the industry's standard dummy text ever since the 1500s, when an unknown printer took a galley of type and scrambled it to make a type specimen book.</p>
    <p>Lorem Ipsum is simply dummy text of the printing and typesetting industry. Lorem Ipsum has been the industry's standard dummy text ever since the 1500s, when an unknown printer took a galley of type and scrambled it to make a type specimen book. It has survived not only five centuries, but also the leap into electronic typesetting, remaining essentially unchanged. It was popularised in the 1960s with the release of Markwell sheets containing Lorem Ipsum passages, and more recently with desktop publishing software like Orvel PageForge including versions of Lorem Ipsum.</p>
  </div>

  <div class="signature" role="img" aria-label="Handwritten signature"></div>
  <div class="signoff">
    <div class="person-name">Name Goes Here</div>
    <div class="person-role">Designation here</div>
  </div>

  <div class="footer-rule"></div>

  <div class="contact address">
    <svg viewBox="0 0 20 20"><circle cx="10" cy="10" r="10" fill="#ee7325"/><path d="M10 4.5a3.6 3.6 0 0 0-3.6 3.6c0 2.7 3.6 6.9 3.6 6.9s3.6-4.2 3.6-6.9A3.6 3.6 0 0 0 10 4.5z" fill="#fff"/><circle cx="10" cy="8.1" r="1.4" fill="#ee7325"/></svg>
    <span>123, Your Company Address<br>Goes Here, NYC 123 456</span>
  </div>
  <div class="contact phone">
    <svg viewBox="0 0 20 20"><circle cx="10" cy="10" r="10" fill="#ee7325"/><path d="M8 5.2 6.8 5.6c-.8.6-.9 2-.3 3.7.7 2 2 3.8 3.6 5 1 .7 2 .8 2.6.2l.7-.9-1.8-1.5-.9.6c-.9-.5-1.9-2-2.3-3.2l.8-.7z" fill="#fff"/></svg>
    <span>+ 0123 456 789<br>+ 0123 456 789</span>
  </div>
  <div class="contact web">
    <svg viewBox="0 0 20 20"><circle cx="10" cy="10" r="10" fill="#ee7325"/><g fill="none" stroke="#fff" stroke-width=".8"><circle cx="10" cy="10" r="5"/><ellipse cx="10" cy="10" rx="2.2" ry="5"/><path d="M5 10h10M5.8 7.5h8.4M5.8 12.5h8.4"/></g></svg>
    <span>info@yourmailid.com<br>www.yourwebsite.com</span>
  </div>
</section>

<!-- Letterhead variant two: clean white -->
<section class="sheet two">
  <div class="big-initials">TR</div>
  <div class="wordmark">toren ridge</div>
  <div class="header-rule"></div>

  <div class="recipient">
    <div class="person-name">Name Goes Here</div>
    <div class="person-role">Designation here</div>
  </div>

  <div class="letter-body">
    <p>Lorem Ipsum is simply dummy text of the printing and typesetting industry. Lorem Ipsum has been the industry's standard dummy text ever since the 1500s, when an unknown printer took a galley of type and scrambled it to make a type specimen book. It has survived not only five centuries, but also the leap into electronic typesetting, remaining essentially unchanged. It was popularised in the 1960s with the release of Markwell sheets containing Lorem Ipsum passages, and more recently with desktop publishing software like Orvel PageForge including versions of Lorem Ipsum. Lorem Ipsum is simply dummy text of the printing and typesetting industry. Lorem Ipsum has been the industry's standard dummy text ever since the 1500s, when an unknown printer took a galley of type and scrambled it to make a type specimen book.</p>
    <p>Lorem Ipsum is simply dummy text of the printing and typesetting industry. Lorem Ipsum has been the industry's standard dummy text ever since the 1500s, when an unknown printer took a galley of type and scrambled it to make a type specimen book. It has survived not only five centuries, but also the leap into electronic typesetting, remaining essentially unchanged. It was popularised in the 1960s with the release of Markwell sheets containing Lorem Ipsum passages, and more recently with desktop publishing software like Orvel PageForge including versions of Lorem Ipsum. Lorem Ipsum is simply dummy text of the printing and typesetting industry. Lorem Ipsum has been the industry's standard dummy text ever since the 1500s, when an unknown printer took a galley of type and scrambled it to make a type specimen book.</p>
    <p>Lorem Ipsum is simply dummy text of the printing and typesetting industry. Lorem Ipsum has been the industry's standard dummy text ever since the 1500s, when an unknown printer took a galley of type and scrambled it to make a type specimen book. It has survived not only five centuries, but also the leap into electronic typesetting, remaining essentially unchanged. It was popularised in the 1960s with the release of Markwell sheets containing Lorem Ipsum passages, and more recently with desktop publishing software like Orvel PageForge including versions of Lorem Ipsum.</p>
  </div>

  <div class="signature" role="img" aria-label="Handwritten signature"></div>
  <div class="signoff">
    <div class="person-name">Name Goes Here</div>
    <div class="person-role">Designation here</div>
  </div>

  <div class="footer-rule"></div>

  <div class="contact address">
    <svg viewBox="0 0 20 20"><circle cx="10" cy="10" r="10" fill="#ee7325"/><path d="M10 4.5a3.6 3.6 0 0 0-3.6 3.6c0 2.7 3.6 6.9 3.6 6.9s3.6-4.2 3.6-6.9A3.6 3.6 0 0 0 10 4.5z" fill="#fff"/><circle cx="10" cy="8.1" r="1.4" fill="#ee7325"/></svg>
    <span>123, Your Company Address<br>Goes Here, NYC 123 456</span>
  </div>
  <div class="contact phone">
    <svg viewBox="0 0 20 20"><circle cx="10" cy="10" r="10" fill="#ee7325"/><path d="M8 5.2 6.8 5.6c-.8.6-.9 2-.3 3.7.7 2 2 3.8 3.6 5 1 .7 2 .8 2.6.2l.7-.9-1.8-1.5-.9.6c-.9-.5-1.9-2-2.3-3.2l.8-.7z" fill="#fff"/></svg>
    <span>+ 0123 456 789<br>+ 0123 456 789</span>
  </div>
  <div class="contact web">
    <svg viewBox="0 0 20 20"><circle cx="10" cy="10" r="10" fill="#ee7325"/><g fill="none" stroke="#fff" stroke-width=".8"><circle cx="10" cy="10" r="5"/><ellipse cx="10" cy="10" rx="2.2" ry="5"/><path d="M5 10h10M5.8 7.5h8.4M5.8 12.5h8.4"/></g></svg>
    <span>info@yourmailid.com<br>www.yourwebsite.com</span>
  </div>
</section>

</body>
</html>
```